Wordpress Site Design for a Horror and Action Movie Production Company

We need a re-design/facelift of our website: https://qz7v.pagebuild.io
The structure of the website could remain the same, but it needs to look and feel BETTER!

We would like the website coded in Wordpress so that it can be easily updated bu us, via adding new projects and new projects' info.

We specialize in Action, Horror, and Sci-Fi Genre. That being said, we don't want the website to look like it's a themed park with haunted houses. It should still be sharp and professional, as after all - it is a business for us!

Target Market(s)

Film Distribution Companies (B2B), as well as general audience that likes movies

Industry/Entity Type

Movie Production

Coding

Coded - Design and coding required

Number of Pages Required

5+ page

Font styles to use
Sans Serif

Colors

Designer to choose colors to be used in the design.

Requirements
Must have
• - PROJECTS page
• - Each PROJECT has a sub-page with project info/updates (up dates could be in a form of a WP post, ideally a template that we can use to update and create new PROJECT pages, with text, poster, and video link (trailer))
• - NEWS page that chronologically lists updates from all PROJECTS (could be done via WP blog)
• - HOME page would
Nice to have
• Should generally have a dark background.
• Websites we like as a reference of general approach and style:
• https://marrowlane.com
• https://velkastudio.com (however this is very image-centric, and we might not have that much imagery at the moment)
• https://www.briarpeakpicturehouse.com/other
• https://quellfilms.com
Should not have
• We specialize in Action, Horror, and Sci-Fi Genre. That being said, we don't want the website to look like it's a themed park with haunted houses. It should still be sharp and professional, as after all - it is a business for us!

```html
<!DOCTYPE html>
<html lang="en">
<head>
<meta charset="utf-8">
<title>Vault Nine Pictures</title>
<link rel="stylesheet" href="https://fonts.googleapis.com/css2?family=Montserrat:ital,wght@0,600;0,700;1,700&family=Merriweather:wght@400;700&display=swap">
<style>
  :root {
    --bg-deep: #1d0a07;
    --bg-warm: #2e130e;
    --ink: #f4efe9;
    --ink-soft: #e2dad2;
    --band: #f2f0ec;
    --band-shade: #b9b5ae;
    --accent-red: #d9321f;
    --accent-yellow: #e3bd0a;
    --accent-teal: #1aa6bc;
    --field: #5c4f4f;
    --submit: #f0cc00;
    --serif: "Merriweather", Georgia, serif;
    --sans: "Montserrat", Arial, sans-serif;
  }
  * { box-sizing: border-box; margin: 0; padding: 0; }
  html, body { width: 1200px; height: 2582px; overflow: hidden; }
  body {
    position: relative;
    background:
      radial-gradient(ellipse at 30% 20%, #3a160f 0%, transparent 55%),
      radial-gradient(ellipse at 75% 70%, #34140e 0%, transparent 55%),
      linear-gradient(180deg, var(--bg-warm), var(--bg-deep));
    color: var(--ink);
    font-family: var(--serif);
  }
  .shapes { position: absolute; left: 0; top: 0; width: 1200px; height: 2582px; }
  .abs { position: absolute; }

  .brand { left: 82px; top: 56px; font-family: var(--sans); font-weight: 600; font-size: 22px; letter-spacing: 1px; color: var(--ink); }
  .site-nav { left: 612px; top: 62px; font-size: 13px; font-weight: 700; letter-spacing: 1.3px; }
  .site-nav a { color: var(--ink); text-decoration: none; position: absolute; white-space: nowrap; }

  .hero-title { left: 0; width: 1160px; top: 226px; text-align: center; font-family: var(--sans); font-weight: 600; font-size: 35px; letter-spacing: 4px; }
  .hero-brand { left: 0; width: 1160px; top: 318px; text-align: center; font-family: var(--sans); font-weight: 600; font-size: 24px; letter-spacing: 1px; }

  .section-title { left: 0; width: 1200px; text-align: center; font-family: var(--sans); font-weight: 700; font-size: 36px; letter-spacing: 4px; }
  .about-copy { left: 100px; width: 950px; top: 682px; text-align: center; font-size: 14px; line-height: 31px; letter-spacing: .4px; color: var(--ink-soft); }
  .about-copy p + p { margin-top: 4px; }

  .pill { height: 33px; line-height: 33px; width: 203px; text-align: center; border-radius: 12px; font-size: 15px; letter-spacing: 1.5px; color: var(--ink); }
  .pill-all { left: 349px; top: 1333px; background: linear-gradient(90deg, #b8561a, #d77a25 50%, #a84c18); }
  .pill-upcoming { left: 641px; top: 1333px; background: linear-gradient(90deg, #6a5a1f, #8a6a24 50%, #5e5520); }

  .news-card { width: 300px; text-align: center; }
  .news-card h3 { font-family: var(--sans); font-style: italic; font-weight: 700; font-size: 20px; letter-spacing: 1.5px; }
  .news-card p { margin-top: 12px; font-size: 14px; line-height: 26px; letter-spacing: .8px; color: var(--ink-soft); }
  .news-card .read-more { display: block; margin-top: 8px; font-size: 14px; letter-spacing: 1.5px; }
  .tone-red h3, .tone-red .read-more { color: var(--accent-red); }
  .tone-yellow h3, .tone-yellow .read-more { color: var(--accent-yellow); }
  .tone-teal h3, .tone-teal .read-more { color: var(--accent-teal); }

  .footer-heading { font-size: 13px; font-weight: 700; letter-spacing: 1.5px; }
  .contact-form label { position: absolute; left: 82px; font-size: 12px; letter-spacing: 1px; }
  .contact-form .field { position: absolute; left: 82px; width: 245px; height: 27px; background: var(--field); font-size: 11.5px; letter-spacing: 1px; padding-left: 8px; line-height: 27px; color: #d8d0ca; }
  .contact-form .submit { position: absolute; left: 82px; top: 2438px; width: 245px; height: 27px; background: var(--submit); color: #2a1a00; font-weight: 700; font-size: 12.5px; letter-spacing: 1.5px; text-align: center; line-height: 27px; }
  .quick-links a { position: absolute; left: 482px; color: var(--ink); text-decoration: none; font-size: 13px; letter-spacing: 1.2px; }
  .footer-about { left: 720px; top: 2186px; width: 355px; font-size: 10px; line-height: 26px; letter-spacing: .4px; text-align: justify; color: var(--ink-soft); }
  .copyright { left: 0; width: 1200px; top: 2500px; text-align: center; font-size: 13.5px; letter-spacing: 1.2px; }
</style>
</head>
<body>
<svg class="shapes" viewBox="0 0 1200 2582">
  <defs>
    <linearGradient id="heroFill" x1="0" y1="0" x2="1" y2="1">
      <stop offset="0" stop-color="#0d3a44"/>
      <stop offset=".3" stop-color="#081a30"/>
      <stop offset=".55" stop-color="#0d2f6e"/>
      <stop offset=".75" stop-color="#08183a"/>
      <stop offset="1" stop-color="#1a62c8"/>
    </linearGradient>
    <radialGradient id="projectsFill" cx=".5" cy=".3" r=".75">
      <stop offset="0" stop-color="#4a4d53"/>
      <stop offset=".55" stop-color="#2a2c31"/>
      <stop offset="1" stop-color="#0f1012"/>
    </radialGradient>
    <radialGradient id="moonFill" cx=".5" cy=".45"><stop offset="0" stop-color="#f2f0ea"/><stop offset=".7" stop-color="#c9c6bf"/><stop offset="1" stop-color="#3a3936"/></radialGradient>
    <radialGradient id="violetFill" cx=".6" cy=".4"><stop offset="0" stop-color="#d4c3d6"/><stop offset=".55" stop-color="#7d5f86"/><stop offset="1" stop-color="#241729"/></radialGradient>
    <linearGradient id="actionFill" x1="0" y1="0" x2="1" y2="1"><stop offset="0" stop-color="#c78a4a"/><stop offset=".4" stop-color="#8d877c"/><stop offset="1" stop-color="#2f2c27"/></linearGradient>
    <radialGradient id="warriorFill" cx=".45" cy=".45"><stop offset="0" stop-color="#c8b08e"/><stop offset=".6" stop-color="#7a6a55"/><stop offset="1" stop-color="#3b3127"/></radialGradient>
    <linearGradient id="hallFill" x1="0" y1="0" x2="1" y2="1"><stop offset="0" stop-color="#3a9c90"/><stop offset=".55" stop-color="#1f6d66"/><stop offset="1" stop-color="#123c39"/></linearGradient>
    <linearGradient id="cityFill" x1="0" y1="0" x2="1" y2="1"><stop offset="0" stop-color="#4a8fc8"/><stop offset=".5" stop-color="#1e3f70"/><stop offset="1" stop-color="#0b1222"/></linearGradient>
  </defs>

  <!-- hero band -->
  <path d="M82,182 Q578,98 1075,182 L1075,189 Q578,135 82,189 Z" fill="var(--band)"/>
  <path d="M82,189 Q578,135 1075,189" fill="none" stroke="var(--band-shade)" stroke-width="3" stroke-dasharray="14 9 4 12"/>
  <path role="img" aria-label="Collage of blue-tinted film stills" d="M82,189 Q578,135 1075,189 L1075,478 Q578,522 82,478 Z" fill="url(#heroFill)"/>
  <path d="M82,478 Q578,522 1075,478 L1075,488 Q578,562 82,488 Z" fill="var(--band)"/>
  <path d="M82,481 Q578,525 1075,481" fill="none" stroke="var(--band-shade)" stroke-width="3" stroke-dasharray="10 14 5 9"/>
  <line x1="489" y1="372" x2="667" y2="372" stroke="var(--ink)" stroke-width="1"/>
  <circle cx="577" cy="420" r="24" fill="none" stroke="var(--ink)" stroke-width="2"/>
  <path d="M571,408 L571,432 L589,420 Z" fill="none" stroke="var(--ink)" stroke-width="2"/>

  <!-- heading rules -->
  <line x1="508" y1="644" x2="688" y2="644" stroke="var(--ink)" stroke-width="1"/>
  <line x1="508" y1="948" x2="688" y2="948" stroke="var(--ink)" stroke-width="1"/>
  <line x1="508" y1="1553" x2="688" y2="1553" stroke="var(--ink)" stroke-width="1"/>

  <!-- projects band -->
  <path d="M80,1042 Q578,948 1075,1042 L1075,1050 Q578,990 80,1050 Z" fill="var(--band)"/>
  <path d="M80,1048 Q578,988 1075,1048" fill="none" stroke="var(--band-shade)" stroke-width="3" stroke-dasharray="16 10 5 13"/>
  <path role="img" aria-label="Misty night scene with dark castle towers" d="M80,1050 Q578,990 1075,1050 L1075,1380 Q578,1440 80,1380 Z" fill="url(#projectsFill)"/>
  <path d="M80,1380 Q578,1440 1075,1380 L1075,1392 Q578,1482 80,1392 Z" fill="var(--band)"/>
  <path d="M80,1384 Q578,1444 1075,1384" fill="none" stroke="var(--band-shade)" stroke-width="3" stroke-dasharray="12 11 6 10"/>
  <circle role="img" aria-label="Horror night project poster with full moon" cx="210" cy="1188" r="114" fill="url(#moonFill)"/>
  <circle role="img" aria-label="Project poster of a hand against a misty window" cx="580" cy="1188" r="114" fill="url(#violetFill)"/>
  <circle role="img" aria-label="Action project still with armed soldiers" cx="948" cy="1188" r="114" fill="url(#actionFill)"/>

  <!-- news artwork -->
  <circle role="img" aria-label="Armoured warrior film still" cx="240" cy="1737" r="136" fill="url(#warriorFill)" stroke="var(--accent-red)" stroke-width="9"/>
  <rect role="img" aria-label="Horror film still in a teal hallway" x="472" y="1632" width="250" height="210" fill="url(#hallFill)" stroke="var(--accent-yellow)" stroke-width="5"/>
  <polygon role="img" aria-label="Sci-fi film still in a neon city" points="935,1614 1058,1848 812,1848" fill="url(#cityFill)" stroke="var(--accent-teal)" stroke-width="8" stroke-linejoin="round"/>

  <!-- footer band -->
  <path d="M82,2108 Q578,2038 1075,2108 L1075,2110 Q578,2072 82,2112 Z" fill="var(--band)"/>
  <path d="M82,2108 Q578,2046 1075,2108" fill="none" stroke="var(--band)" stroke-width="6" stroke-dasharray="30 8 12 6"/>
  <line x1="82" y1="2565" x2="1075" y2="2565" stroke="var(--ink)" stroke-width="1"/>
</svg>

<header>
  <div class="abs brand">VAULT NINE PICTURES</div>
  <nav class="abs site-nav">
    <a style="left:0">HOME</a>
    <a style="left:90px">ABOUT US</a>
    <a style="left:196px;top:-1px">PROJECTS</a>
    <a style="left:318px">NEWS</a>
    <a style="left:391px">CONTACT</a>
  </nav>
</header>

<section class="hero">
  <div class="abs hero-title">WELCOME TO</div>
  <div class="abs hero-brand">VAULT NINE PICTURES</div>
</section>

<section class="about">
  <h2 class="abs section-title" style="top:594px">ABOUT US</h2>
  <div class="abs about-copy">
    <p>Vault Nine Pictures is a fresh brand of multi-media entertainment, aimed at development of original Canadian content as well as servicing of foreign productions in Toronto, Ontario, Canada.</p>
    <p>We produce genre feature films, series, documentaries, and anything else that we feel great about. We take pride in our innovative approach to the process of filmmaking and marketing of our produced content. In simple terms, we make good looking motion picture content that is entertaining, visually compelling, and tells a good story.</p>
  </div>
</section>

<section class="projects">
  <h2 class="abs section-title" style="top:898px">PROJECTS</h2>
  <div class="abs pill pill-all">All Projects</div>
  <div class="abs pill pill-upcoming">Upcoming Projects</div>
</section>

<section class="news">
  <h2 class="abs section-title" style="top:1503px">NEWS</h2>
  <article class="abs news-card tone-red" style="left:90px;top:1898px">
    <h3>Lorem Ipsum</h3>
    <p>Lorem Ipsum has been the industry's standard dummy text ever since the</p>
    <span class="read-more">Read More</span>
  </article>
  <article class="abs news-card tone-yellow" style="left:430px;top:1897px">
    <h3>Lorem Ipsum</h3>
    <p>Lorem Ipsum has been the industry's standard dummy text ever since the</p>
    <span class="read-more">Read More</span>
  </article>
  <article class="abs news-card tone-teal" style="left:782px;top:1896px">
    <h3>Lorem Ipsum</h3>
    <p>Lorem Ipsum has been the industry's standard dummy text ever since the</p>
    <span class="read-more">Read More</span>
  </article>
</section>

<footer>
  <div class="abs footer-heading" style="left:82px;top:2150px">CONTACT US</div>
  <div class="contact-form">
    <label style="top:2189px">Name :</label>
    <div class="field" style="top:2221px">Name</div>
    <label style="top:2268px">Email Id :</label>
    <div class="field" style="top:2297px;padding-left:0">Email Id</div>
    <label style="top:2351px">Message :</label>
    <div class="field" style="top:2380px;padding-left:0">Message</div>
    <div class="submit">Submit</div>
  </div>

  <div class="abs footer-heading" style="left:482px;top:2150px">QUICK LINKS</div>
  <nav class="quick-links">
    <a style="top:2188px;left:483px">Home</a>
    <a style="top:2231px;left:483px">About US</a>
    <a style="top:2271px">Projects</a>
    <a style="top:2314px">News</a>
    <a style="top:2356px">Contact us</a>
  </nav>

  <div class="abs footer-heading" style="left:720px;top:2150px">ABOUT</div>
  <p class="abs footer-about">All the information on this website is published in good faith and for general information purpose only. Vault Nine Pictures Inc. does not make any warranties about the completeness, reliability and accuracy of this information. Any action you take upon the information you find on this website is strictly at your own risk. will not be liable for any losses and/or damages in connection with the use of our website.</p>

  <p class="abs copyright">(C) 2019 Vault Nine Pictures Inc. All rights reserved.</p>
</footer>
</body>
</html>
```